Corvelle Strategies business card

I need a business card for my new strategic consulting LLC, Corvelle Strategies. We specialize in helping people who care about broadband technology and telecommunications policy, and we're based in Washington DC. I'm looking for a card that says smart, credible, future-facing and signals a high level of expertise. It's DC, so there's clearly a limit to how crazy we can go with this card, but I am looking for a design that reflects a company that is comfortable with technology, policy, and having a little bit fun. I'm uploading my logo below, and I'd like to have it be part of the card design in some fashion.
Target Market(s)
Telecommunications and technology policy professionals
Industry/Entity Type
Technology policy
Contact Information for Business Card
Name of business, my name (Glen Mosswater), email (glen@corvellestrategies-example.com) , phone number (202-555-0148)phone number

```html
<!DOCTYPE html>
<html lang="en">
<head>
<meta charset="UTF-8">
<title>Corvelle Strategies Business Card</title>
<link rel="stylesheet" href="https://fonts.googleapis.com/css2?family=Oswald:wght@600&family=Nunito+Sans:wght@400&display=swap">
<style>
  :root {
    --page-bg: #f3f3f5;
    --card-white: #ffffff;
    --brand-blue: #1f65a0;
    --deep-blue: #234f7a;
    --sun-gold: #f0bd55;
    --text-light: #ffffff;
    --card-shadow: rgba(20, 30, 50, 0.18);
  }
  * { margin: 0; padding: 0; box-sizing: border-box; }
  html, body {
    width: 1200px;
    height: 900px;
    overflow: hidden;
    background: var(--page-bg);
  }
  .card-set {
    width: 1200px;
    height: 900px;
    display: flex;
    align-items: center;
    justify-content: center;
    gap: 44px;
  }
  .card {
    width: 525px;
    height: 300px;
    border-radius: 4px;
    box-shadow: 0 10px 28px var(--card-shadow);
    position: relative;
    overflow: hidden;
  }
  .card-back {
    background: var(--brand-blue);
    color: var(--text-light);
  }
  .wave-decoration {
    position: absolute;
    left: 230px;
    top: 205px;
    width: 270px;
    height: 120px;
    border-radius: 60% 40% 0 0 / 80% 70% 0 0;
    background: linear-gradient(160deg, var(--deep-blue) 0%, rgba(35, 79, 122, 0.75) 100%);
  }
  .sun-mark {
    position: absolute;
    left: 36px;
    top: 226px;
    width: 34px;
    height: 34px;
    border-radius: 50%;
    background: var(--sun-gold);
  }
  .contact-block {
    position: absolute;
    left: 110px;
    top: 30px;
  }
  .person-name {
    font-family: 'Oswald', sans-serif;
    font-weight: 600;
    font-size: 46px;
    line-height: 1;
    letter-spacing: -0.5px;
    text-transform: uppercase;
  }
  .email-line {
    font-family: 'Nunito Sans', sans-serif;
    font-size: 14px;
    line-height: 1.2;
    margin-top: 10px;
  }
  .phone-line {
    font-family: 'Nunito Sans', sans-serif;
    font-size: 34px;
    line-height: 1.2;
    margin-top: 2px;
    letter-spacing: 1px;
  }
  .city-line {
    font-family: 'Oswald', sans-serif;
    font-weight: 600;
    font-size: 24px;
    line-height: 1.2;
    text-transform: uppercase;
    margin-top: 2px;
  }
  .card-front {
    background: var(--card-white);
    display: flex;
    align-items: center;
    justify-content: center;
    gap: 16px;
  }
  .brand-name {
    font-family: 'Oswald', sans-serif;
    font-weight: 600;
    font-size: 40px;
    color: var(--brand-blue);
    text-transform: uppercase;
    letter-spacing: 1px;
  }
  .brand-dot {
    width: 30px;
    height: 30px;
    border-radius: 50%;
    background: var(--sun-gold);
  }
</style>
</head>
<body>
  <main class="card-set">
    <section class="card card-back" aria-label="Card back with contact details">
      <div class="wave-decoration" role="img" aria-label="Large dark blue river swoosh decoration"></div>
      <div class="sun-mark"></div>
      <div class="contact-block">
        <h1 class="person-name">Glen Mosswater</h1>
        <p class="email-line">email (glen@corvellestrategies-example.com)</p>
        <p class="phone-line">202-555-0148</p>
        <p class="city-line">Washington DC</p>
      </div>
    </section>
    <section class="card card-front" aria-label="Card front with company name">
      <span class="brand-name">Corvelle Strategies</span>
      <span class="brand-dot"></span>
    </section>
  </main>
</body>
</html>
```